PowerPoint Template - Multiple Slide Backgrounds

Looking for a professional PowerPoint template for a technology company. You will see with the logo there's sort of a theme with gears and a lightbulb of sorts. Keeping with this sort of design could help with the brand.

Branding information
• Logo with transparent background included
• Primary Color (Orange) Hex #E6753D
• Secondary Color (Brown) Hex #6A4238
• Primary Font - Myriad Pro
• Secondary Font - Quiet Sans Light

Design request -
• PowerPoint (POTX) template with master slide views
• Cover Slide
• Color Pallet - 7 Color PowerPoint pallet that includes and complements primary and secondary colors
• Slide Master with Footer
• Multiple Background Types to allow for smart art overlay or bullet point text boxes
Bonus - Sample graphical elements using shapes and smart art

```html
<!DOCTYPE html>
<html lang="en">
<head>
<meta charset="utf-8">
<title>Cedar Loop Labs – Presentation Template</title>
<link href="https://fonts.googleapis.com/css2?family=Roboto:wght@400;500;700&family=Open+Sans:ital,wght@0,400;0,600;0,700;1,400&display=swap" rel="stylesheet">
<style>
  :root{
    --brown:#6A4238;
    --brown-dark:#55332b;
    --orange:#E6753D;
    --peach:#F2B48A;
    --peach-light:#F7CFAE;
    --slate:#5d7d97;
    --navy:#2d3a56;
    --paper:#f1f1f1;
    --paper-shade:#dedede;
    --ink:#3a3a3a;
    --stage:#f3efea;
  }
  *{margin:0;padding:0;box-sizing:border-box}
  html,body{width:1062px;height:1200px;overflow:hidden;background:var(--stage)}
  body{position:relative;font-family:"Open Sans",Arial,sans-serif;color:var(--ink)}
  .slide{position:absolute;width:480px;height:270px;overflow:hidden;
    background:linear-gradient(160deg,#fafafa 0%,var(--paper) 45%,var(--paper-shade) 100%);
    box-shadow:0 3px 8px rgba(0,0,0,.25)}
  .col-left{left:44px}.col-right{left:538px}
  .row-1{top:14px}.row-2{top:306px}.row-3{top:598px}.row-4{top:890px}
  .slide-header{position:absolute;left:0;top:0;width:480px;height:44px}
  .slide-title{position:absolute;left:22px;top:7px;font-family:"Roboto",Arial,sans-serif;font-weight:500;font-size:21px;color:#fff;letter-spacing:.2px}
  .brand{position:absolute;right:10px;top:4px;width:84px;display:flex;flex-direction:column;align-items:center;gap:3px}
  .brand-mark{width:22px;height:22px;border-radius:50%;background:var(--orange)}
  .brand-name{font-family:"Roboto",Arial,sans-serif;font-weight:700;font-size:9.5px;color:var(--brown);white-space:nowrap}
  .slide-footer{position:absolute;left:0;bottom:10px;width:480px;height:8px}
  .page-no{position:absolute;left:50px;bottom:9px;font-family:"Roboto",Arial,sans-serif;font-size:7px;font-weight:700;color:#333}
  .chart{position:absolute;left:0;top:0;width:480px;height:270px}
  .chart text{font-family:"Open Sans",Arial,sans-serif}
  .caption{position:absolute;font-size:6.4px;line-height:1.35;color:#333;text-align:center}
  .feature{position:absolute;top:117px;width:56px;font-size:6.6px;line-height:1.3;color:#222}
  .feature h3{font-family:"Roboto",Arial,sans-serif;font-size:7.4px;font-weight:700;color:var(--brown);margin-bottom:2px;text-align:center}
  .side-text{position:absolute;left:320px;top:82px;width:128px;font-size:6.2px;line-height:1.3;text-align:justify;color:#333}
  .side-text p+p{margin-top:6px}
  .data-table{position:absolute;left:24px;top:70px;width:430px;border-collapse:separate;border-spacing:1.5px;background:#fff}
  .data-table th{height:20px;background:var(--brown)}
  .data-table td{height:21px;background:#cfcfcf}
  .data-table td.row-head{background:var(--peach);width:42px}
  .text-col{position:absolute;top:190px;width:196px;font-size:6.2px;line-height:1.3;color:#222}
  .title-dark{position:absolute;left:26px;top:32px;font-family:"Roboto",Arial,sans-serif;font-weight:500;font-size:21px;color:var(--brown)}
  .quote-band{position:absolute;left:0;top:88px;width:480px;height:110px;background:var(--brown)}
  .quote-notch{position:absolute;left:34px;top:84px;width:0;height:0;border-left:6px solid transparent;border-right:6px solid transparent;border-bottom:5px solid var(--brown)}
  .quote-mark{position:absolute;font-family:"Roboto",Arial,sans-serif;font-weight:700;font-size:40px;color:#c9b3ab;line-height:1}
  .quote-text{position:absolute;left:76px;top:100px;width:276px;font-style:italic;font-size:5.8px;line-height:1.4;color:#fff;text-align:center}
  .portrait{position:absolute;left:206px;top:166px;width:72px;height:72px;border-radius:50%;background:#fff;border:3px solid var(--orange);padding:3px}
  .portrait span{display:block;width:100%;height:100%;border-radius:50%;background:radial-gradient(circle at 50% 40%,#cfd6df,#6b7a8c)}
  .circuit-art{position:absolute;left:0;top:0;width:480px;height:221px;background:radial-gradient(ellipse at 62% 55%,#dff1f4 0%,#eef4f6 45%,#f4f4f4 100%)}
  .headline-big{position:absolute;left:22px;top:86px;font-family:"Roboto",Arial,sans-serif;font-weight:400;font-size:37px;letter-spacing:.5px;color:var(--navy)}
  .contact-band{position:absolute;left:0;top:221px;width:480px;height:49px;background:linear-gradient(180deg,var(--brown),var(--brown-dark))}
  .contact{position:absolute;display:flex;align-items:center;gap:4px;font-size:7px;color:#fff}
  .contact svg{width:8px;height:8px}
  .thanks{position:absolute;right:14px;top:226px;text-align:right;font-family:"Roboto",Arial,sans-serif;line-height:1.05}
  .thanks strong{display:block;font-weight:400;font-size:18px;color:var(--orange)}
  .thanks span{font-size:14px;color:#fff}
</style>
</head>
<body>

<!-- Slide: icon features -->
<section class="slide col-left row-1">
  <svg class="slide-header" viewBox="0 0 480 44"><polygon points="0,0 370,0 344,40 0,40" fill="var(--brown)"/><polygon points="374,0 386,0 360,40 348,40" fill="var(--orange)"/><polygon points="390,0 399,0 373,40 364,40" fill="var(--peach)"/><polygon points="403,0 409,0 383,40 377,40" fill="var(--peach-light)"/></svg>
  <h1 class="slide-title">Iconic Slide</h1>
  <div class="brand"><span class="brand-mark"></span><span class="brand-name">Cedar Loop Labs</span></div>
  <svg class="chart" viewBox="0 0 480 270" fill="none" stroke="#fff" stroke-width="1.6" stroke-linecap="round" stroke-linejoin="round">
    <g fill="var(--brown)" stroke="none">
      <circle cx="59" cy="92" r="22"/><circle cx="119" cy="92" r="22"/><circle cx="179" cy="92" r="22"/><circle cx="239" cy="92" r="22"/><circle cx="299" cy="92" r="22"/><circle cx="359" cy="92" r="22"/><circle cx="419" cy="92" r="22"/>
    </g>
    <g><circle cx="59" cy="92" r="5"/><path d="M59 80v5M59 99v5M47 92h5M66 92h5M51 84l3.5 3.5M63.5 96.5l3.5 3.5M67 84l-3.5 3.5M54.5 96.5L51 100"/></g>
    <g><rect x="111" y="84" width="16" height="16" rx="1.5"/><rect x="115" y="88" width="8" height="8"/><path d="M115 80v4M119 80v4M123 80v4M115 100v4M119 100v4M123 100v4M107 88h4M107 96h4M127 88h4M127 96h4"/></g>
    <g><ellipse cx="179" cy="83" rx="9" ry="3.5"/><path d="M170 83v18c0 2 4 3.5 9 3.5s9-1.5 9-3.5V83M170 89c0 2 4 3.5 9 3.5s9-1.5 9-3.5M170 95c0 2 4 3.5 9 3.5s9-1.5 9-3.5"/></g>
    <g><path d="M239 79l10 4v7c0 7-5 11-10 13-5-2-10-6-10-13v-7z"/><path d="M234.5 91l3 3 6-6"/></g>
    <g><path d="M286 88a19 19 0 0 1 26 0M290 93a13 13 0 0 1 18 0M294 98a7 7 0 0 1 10 0"/><circle cx="299" cy="102" r="1.2" fill="#fff"/></g>
    <g><path d="M369 81l-20 9 9 3 3 9z"/></g>
    <g><circle cx="419" cy="83" r="4"/><path d="M412 96c0-4 3-6 7-6s7 2 7 6M408 103h6l5-3h5M408 99l6 4"/></g>
  </svg>
  <div class="feature" style="left:31px"><h3>Lorem Ipsum</h3>Lorem ipsum dolor sit amet, consectetur adipiscing elit. Ut enim ad minim veniam, quis nostrud exercitation ullamco laboris nisi ut aliquip consequat.</div>
  <div class="feature" style="left:91px"><h3>Lorem Ipsum</h3>Lorem ipsum dolor sit amet, consectetur adipiscing elit. Ut enim ad minim veniam, quis nostrud exercitation ullamco laboris nisi ut aliquip consequat.</div>
  <div class="feature" style="left:151px"><h3>Lorem Ipsum</h3>Lorem ipsum dolor sit amet, consectetur adipiscing elit. Ut enim ad minim veniam, quis nostrud exercitation ullamco laboris nisi ut aliquip consequat.</div>
  <div class="feature" style="left:211px"><h3>Lorem Ipsum</h3>Lorem ipsum dolor sit amet, consectetur adipiscing elit. Ut enim ad minim veniam, quis nostrud exercitation ullamco laboris nisi ut aliquip consequat.</div>
  <div class="feature" style="left:271px"><h3>Lorem Ipsum</h3>Lorem ipsum dolor sit amet, consectetur adipiscing elit. Ut enim ad minim veniam, quis nostrud exercitation ullamco laboris nisi ut aliquip consequat.</div>
  <div class="feature" style="left:331px"><h3>Lorem Ipsum</h3>Lorem ipsum dolor sit amet, consectetur adipiscing elit. Ut enim ad minim veniam, quis nostrud exercitation ullamco laboris nisi ut aliquip consequat.</div>
  <div class="feature" style="left:391px"><h3>Lorem Ipsum</h3>Lorem ipsum dolor sit amet, consectetur adipiscing elit. Ut enim ad minim veniam, quis nostrud exercitation ullamco laboris nisi ut aliquip consequat.</div>
  <svg class="slide-footer" viewBox="0 0 480 8"><polygon points="0,1 44,1 40,7 0,7" fill="var(--brown)"/><polygon points="64,1 480,1 480,7 60,7" fill="var(--orange)"/></svg>
  <span class="page-no">1</span>
</section>

<!-- Slide: area chart -->
<section class="slide col-right row-1">
  <svg class="slide-header" viewBox="0 0 480 44"><polygon points="0,0 370,0 344,40 0,40" fill="var(--brown)"/><polygon points="374,0 386,0 360,40 348,40" fill="var(--orange)"/><polygon points="390,0 399,0 373,40 364,40" fill="var(--peach)"/><polygon points="403,0 409,0 383,40 377,40" fill="var(--peach-light)"/></svg>
  <h1 class="slide-title">Graphics Chart</h1>
  <div class="brand"><span class="brand-mark"></span><span class="brand-name">Cedar Loop Labs</span></div>
  <svg class="chart" viewBox="0 0 480 270">
    <g font-size="5" fill="#555">
      <rect x="330" y="73" width="4" height="4" fill="#cdd9f0"/><text x="336" y="77">2015</text>
      <rect x="354" y="73" width="4" height="4" fill="#9fb6e0"/><text x="360" y="77">2016</text>
      <rect x="378" y="73" width="4" height="4" fill="#6a86c4"/><text x="384" y="77">2017</text>
      <rect x="402" y="73" width="4" height="4" fill="#4a5d8f"/><text x="408" y="77">2018</text>
    </g>
    <g stroke="#d6d6d6" stroke-width=".5"><line x1="58" y1="106" x2="433" y2="106"/><line x1="58" y1="126.75" x2="433" y2="126.75"/><line x1="58" y1="147.5" x2="433" y2="147.5"/><line x1="58" y1="168.25" x2="433" y2="168.25"/><line x1="58" y1="189" x2="433" y2="189"/></g>
    <g font-size="4.5" fill="#777" text-anchor="end"><text x="54" y="108">400</text><text x="54" y="129">300</text><text x="54" y="149">200</text><text x="54" y="170">100</text><text x="54" y="191">0</text></g>
    <polygon points="58,148 110,150 165,152 220,136 285,140 340,116 433,170 433,189 58,189" fill="#4a5d8f"/>
    <polygon points="58,160 165,158 285,152 340,150 433,172 433,189 58,189" fill="#6a86c4"/>
    <polygon points="58,168 220,164 340,160 433,176 433,189 58,189" fill="#9fb6e0"/>
    <polygon points="58,176 220,172 340,170 433,180 433,189 58,189" fill="#cdd9f0"/>
    <g font-size="4" fill="#777" text-anchor="middle"><text x="58" y="197">JAN</text><text x="92" y="197">FEB</text><text x="126" y="197">MAR</text><text x="160" y="197">APR</text><text x="194" y="197">MAY</text><text x="228" y="197">JUN</text><text x="263" y="197">JUL</text><text x="297" y="197">AUG</text><text x="331" y="197">SEP</text><text x="365" y="197">OCT</text><text x="399" y="197">NOV</text><text x="433" y="197">DEC</text></g>
  </svg>
  <p class="caption" style="left:80px;top:216px;width:330px">Lorem ipsum dolor sit amet, consectetur adipiscing elit, sed do eiusmod tempor incididunt ut labore et dolore magna aliqua. Ut enim ad minim veniam, quis nostrud exercitation ullamco laboris nisi ut aliquip ex ea commodo.</p>
  <svg class="slide-footer" viewBox="0 0 480 8"><polygon points="0,1 44,1 40,7 0,7" fill="var(--brown)"/><polygon points="64,1 480,1 480,7 60,7" fill="var(--orange)"/></svg>
  <span class="page-no">1</span>
</section>

<!-- Slide: triangle chart -->
<section class="slide col-left row-2">
  <svg class="slide-header" viewBox="0 0 480 44"><polygon points="0,0 370,0 344,40 0,40" fill="var(--brown)"/><polygon points="374,0 386,0 360,40 348,40" fill="var(--orange)"/><polygon points="390,0 399,0 373,40 364,40" fill="var(--peach)"/><polygon points="403,0 409,0 383,40 377,40" fill="var(--peach-light)"/></svg>
  <h1 class="slide-title">Traingle Chart</h1>
  <div class="brand"><span class="brand-mark"></span><span class="brand-name">Cedar Loop Labs</span></div>
  <svg class="chart" viewBox="0 0 480 270">
    <g stroke="#333" stroke-width=".7"><line x1="38" y1="59" x2="38" y2="219"/><line x1="38" y1="219" x2="297" y2="219"/>
      <path d="M35 59h3M35 91h3M35 123h3M35 155h3M35 187h3"/></g>
    <g font-size="5.5" fill="#333" text-anchor="end"><text x="32" y="61">150</text><text x="32" y="93">120</text><text x="32" y="125">90</text><text x="32" y="157">60</text><text x="32" y="189">30</text><text x="32" y="221">0</text></g>
    <polygon points="58,214 77,123 96,214" fill="#9b908e"/>
    <polygon points="101,214 120,101.6 139,214" fill="#e98752"/>
    <polygon points="144,214 163,152.8 182,214" fill="#9ec7cc"/>
    <polygon points="187,214 206,123 225,214" fill="#5bb6e3"/>
    <polygon points="229,214 248,88.8 267,214" fill="var(--slate)"/>
    <polygon points="272,214 291,59 310,214" fill="#9a5a50"/>
    <g font-size="5.5" fill="#333" text-anchor="middle"><text x="77" y="229">2016</text><text x="120" y="229">2017</text><text x="163" y="229">2018</text><text x="206" y="229">2019</text><text x="248" y="229">2020</text><text x="291" y="229">2021</text></g>
  </svg>
  <div class="side-text">
    <p>Lorem Ipsum is simply dummy text of the printing and typesetting industry. Lorem Ipsum has been the industry's standard dummy text ever since the 1500s, when an unknown printer took a galley of type and scrambled it to make a type specimen book.</p>
    <p>Contrary to popular belief, Lorem Ipsum is not simply random text. It has roots in a piece of classical Latin literature from 45 BC, making it over 2000 years old. Mara Ellison, a Latin teacher at Westbrook Academy.</p>
  </div>
  <svg class="slide-footer" viewBox="0 0 480 8"><polygon points="0,1 44,1 40,7 0,7" fill="var(--brown)"/><polygon points="64,1 480,1 480,7 60,7" fill="var(--orange)"/></svg>
  <span class="page-no">1</span>
</section>

<!-- Slide: pie charts -->
<section class="slide col-right row-2">
  <svg class="slide-header" viewBox="0 0 480 44"><polygon points="0,0 370,0 344,40 0,40" fill="var(--brown)"/><polygon points="374,0 386,0 360,40 348,40" fill="var(--orange)"/><polygon points="390,0 399,0 373,40 364,40" fill="var(--peach)"/><polygon points="403,0 409,0 383,40 377,40" fill="var(--peach-light)"/></svg>
  <h1 class="slide-title">Pie Chart</h1>
  <div class="brand"><span class="brand-mark"></span><span class="brand-name">Cedar Loop Labs</span></div>
  <svg class="chart" viewBox="0 0 480 270">
    <path d="M94 152L94 110A42 42 0 1 1 69.3 186Z" fill="var(--brown)"/>
    <path d="M94 152L69.3 186A42 42 0 0 1 94 110Z" fill="var(--orange)"/>
    <path d="M207 152L207 110A42 42 0 0 1 241 176.7Z" fill="var(--brown)"/>
    <path d="M207 152L241 176.7A42 42 0 0 1 182.3 186Z" fill="var(--orange)"/>
    <path d="M207 152L182.3 186A42 42 0 0 1 207 110Z" fill="#e9a96d"/>
    <path d="M322 152L322 110A42 42 0 0 1 361.9 139Z" fill="var(--brown)"/>
    <path d="M322 152L361.9 139A42 42 0 0 1 346.7 186Z" fill="var(--orange)"/>
    <path d="M322 152L346.7 186A42 42 0 0 1 282.1 139Z" fill="#a3a3a3"/>
    <path d="M322 152L282.1 139A42 42 0 0 1 322 110Z" fill="#e9a96d"/>
    <g font-size="5" font-weight="700" fill="#fff" text-anchor="middle">
      <rect x="97" y="83" width="16" height="8" fill="var(--brown)"/><text x="105" y="89">60%</text>
      <rect x="77" y="97" width="16" height="8" fill="var(--orange)"/><text x="85" y="103">40%</text>
      <rect x="189" y="69" width="16" height="8" fill="#e9a96d"/><text x="197" y="75">40%</text>
      <rect x="212" y="83" width="16" height="8" fill="var(--brown)"/><text x="220" y="89">35%</text>
      <rect x="189" y="97" width="16" height="8" fill="var(--orange)"/><text x="197" y="103">25%</text>
      <rect x="324" y="55" width="16" height="8" fill="#a3a3a3"/><text x="332" y="61">40%</text>
      <rect x="303" y="69" width="16" height="8" fill="var(--orange)"/><text x="311" y="75">20%</text>
      <rect x="324" y="83" width="16" height="8" fill="var(--brown)"/><text x="332" y="89">20%</text>
      <rect x="303" y="97" width="16" height="8" fill="#e9a96d"/><text x="311" y="103">20%</text>
    </g>
  </svg>
  <p class="caption" style="left:40px;top:212px;width:400px">Lorem Ipsum is simply dummy text of the printing and typesetting industry. Lorem Ipsum has been the industry's standard dummy text ever since the 1500s, when an unknown printer took a galley of type and scrambled it to make a type specimen book.</p>
  <svg class="slide-footer" viewBox="0 0 480 8"><polygon points="0,1 44,1 40,7 0,7" fill="var(--brown)"/><polygon points="64,1 480,1 480,7 60,7" fill="var(--orange)"/></svg>
  <span class="page-no">1</span>
</section>

<!-- Slide: pyramid -->
<section class="slide col-left row-3">
  <svg class="slide-header" viewBox="0 0 480 44"><polygon points="0,0 370,0 344,40 0,40" fill="var(--brown)"/><polygon points="374,0 386,0 360,40 348,40" fill="var(--orange)"/><polygon points="390,0 399,0 373,40 364,40" fill="var(--peach)"/><polygon points="403,0 409,0 383,40 377,40" fill="var(--peach-light)"/></svg>
  <h1 class="slide-title">Graphics Chart</h1>
  <div class="brand"><span class="brand-mark"></span><span class="brand-name">Cedar Loop Labs</span></div>
  <svg class="chart" viewBox="0 0 480 270">
    <g stroke="#9a9a9a" stroke-width=".5"><line x1="82" y1="82" x2="226" y2="82"/><line x1="82" y1="111" x2="205" y2="111"/><line x1="82" y1="141" x2="186" y2="141"/><line x1="82" y1="170" x2="168" y2="170"/>
      <line x1="250" y1="82" x2="396" y2="82"/><line x1="271" y1="111" x2="396" y2="111"/><line x1="290" y1="141" x2="396" y2="141"/><line x1="308" y1="170" x2="396" y2="170"/></g>
    <polygon points="238,67 219.25,96.75 238,96.75" fill="#8a5a3c"/>
    <polygon points="219.75,97.75 238,97.75 238,126.5 201,126.5" fill="#ef8f4e"/>
    <polygon points="200.5,127.5 238,127.5 238,156.25 182.25,156.25" fill="#f6b27f"/>
    <polygon points="181.75,157.25 238,157.25 238,186 163,186" fill="#f6c79d"/>
    <polygon points="238,67 256.75,96.75 238,96.75" fill="#5c6b7d"/>
    <polygon points="256.25,97.75 238,97.75 238,126.5 275,126.5" fill="#7f90a3"/>
    <polygon points="275.5,127.5 238,127.5 238,156.25 293.75,156.25" fill="#a5b4c4"/>
    <polygon points="294.25,157.25 238,157.25 238,186 313,186" fill="#c0cad5"/>
    <g font-size="5" fill="#333"><text x="40" y="84">Lorem ipsum</text><text x="40" y="113">Lorem ipsum</text><text x="40" y="143">Lorem ipsum</text><text x="40" y="172">Lorem ipsum</text>
      <text x="400" y="84">Lorem ipsum</text><text x="400" y="113">Lorem ipsum</text><text x="400" y="143">Lorem ipsum</text><text x="400" y="172">Lorem ipsum</text></g>
  </svg>
  <p class="caption" style="left:66px;top:206px;width:350px">Lorem Ipsum is simply dummy text of the printing and typesetting industry. Lorem Ipsum has been the industry's standard dummy text ever since the 1500s, when an unknown printer took a galley of type and scrambled it to make a type specimen book.</p>
  <svg class="slide-footer" viewBox="0 0 480 8"><polygon points="0,1 44,1 40,7 0,7" fill="var(--brown)"/><polygon points="64,1 480,1 480,7 60,7" fill="var(--orange)"/></svg>
  <span class="page-no">1</span>
</section>

<!-- Slide: table -->
<section class="slide col-right row-3">
  <svg class="slide-header" viewBox="0 0 480 44"><polygon points="0,0 370,0 344,40 0,40" fill="var(--brown)"/><polygon points="374,0 386,0 360,40 348,40" fill="var(--orange)"/><polygon points="390,0 399,0 373,40 364,40" fill="var(--peach)"/><polygon points="403,0 409,0 383,40 377,40" fill="var(--peach-light)"/></svg>
  <h1 class="slide-title">Headline Goes Here</h1>
  <div class="brand"><span class="brand-mark"></span><span class="brand-name">Cedar Loop Labs</span></div>
  <table class="data-table">
    <tr><th></th><th></th><th></th><th></th><th></th><th></th><th></th><th></th><th></th><th></th></tr>
    <tr><td class="row-head"></td><td></td><td></td><td></td><td></td><td></td><td></td><td></td><td></td><td></td></tr>
    <tr><td class="row-head"></td><td></td><td></td><td></td><td></td><td></td><td></td><td></td><td></td><td></td></tr>
    <tr><td class="row-head"></td><td></td><td></td><td></td><td></td><td></td><td></td><td></td><td></td><td></td></tr>
    <tr><td class="row-head"></td><td></td><td></td><td></td><td></td><td></td><td></td><td></td><td></td><td></td></tr>
  </table>
  <p class="text-col" style="left:34px">Lorem Ipsum is simply dummy text of the printing and typesetting industry. Lorem Ipsum has been the industry's standard dummy text ever since the 1500s, when an unknown printer took a galley of type and scrambled.Lorem Ipsum is simply dummy text of the printing.</p>
  <p class="text-col" style="left:250px">Lorem Ipsum is simply dummy text of the printing and typesetting industry. Lorem Ipsum has been the industry's standard dummy text ever since the 1500s, when an unknown printer took a galley of type and scrambled.Lorem Ipsum is simply dummy text of the printing.</p>
  <svg class="slide-footer" viewBox="0 0 480 8"><polygon points="0,1 44,1 40,7 0,7" fill="var(--brown)"/><polygon points="64,1 480,1 480,7 60,7" fill="var(--orange)"/></svg>
  <span class="page-no">1</span>
</section>

<!-- Slide: testimonial -->
<section class="slide col-left row-4">
  <h1 class="title-dark">Client Testimonials</h1>
  <div class="brand" style="top:22px"><span class="brand-mark"></span><span class="brand-name">Cedar Loop Labs</span></div>
  <span class="quote-notch"></span>
  <div class="quote-band"></div>
  <span class="quote-mark" style="left:46px;top:94px">“</span>
  <span class="quote-mark" style="left:352px;top:152px">”</span>
  <p class="quote-text">It is a long established fact that a reader will be distracted by the readable content of a page when looking at its layout. The point of using Lorem Ipsum is that it has a more-or-less normal distribution of letters, as opposed to using 'Content here, content here', making it look like readable English. Many desktop publishing packages and web page editors now use Lorem Ipsum as their default model text, and a search for 'lorem ipsum' will uncover many web sites still in their infancy. Various versions have evolved over the years, sometimes accident, sometimes on purpose (injected humour and the like).</p>
  <div class="portrait"><span role="img" aria-label="Client portrait photo"></span></div>
  <svg class="slide-footer" viewBox="0 0 480 8"><polygon points="0,1 44,1 40,7 0,7" fill="var(--brown)"/><polygon points="64,1 480,1 480,7 60,7" fill="var(--orange)"/></svg>
  <span class="page-no">1</span>
</section>

<!-- Slide: closing -->
<section class="slide col-right row-4">
  <div class="circuit-art" role="img" aria-label="Light circuit-board illustration with teal and orange rings"></div>
  <h2 class="headline-big">TECHNOLOGY</h2>
  <div class="brand" style="top:26px"><span class="brand-mark"></span><span class="brand-name">Cedar Loop Labs</span></div>
  <div class="contact-band"></div>
  <div class="contact" style="left:22px;top:232px"><svg viewBox="0 0 8 8"><path d="M1.5 1l1.5-.5 1 2-1 .8c.4 1 1 1.6 2 2l.8-1 2 1L7.3 7C4 7 1 4 1.5 1z" fill="var(--orange)"/></svg>4570-2210-6634</div>
  <div class="contact" style="left:96px;top:232px"><svg viewBox="0 0 8 8"><path d="M1.5 1l1.5-.5 1 2-1 .8c.4 1 1 1.6 2 2l.8-1 2 1L7.3 7C4 7 1 4 1.5 1z" fill="var(--orange)"/></svg>4410-381-2290</div>
  <div class="contact" style="left:22px;top:248px"><svg viewBox="0 0 8 8"><rect x=".5" y="1.5" width="7" height="5" fill="var(--orange)"/><path d="M.5 1.5L4 4.5l3.5-3" stroke="#fff" stroke-width=".6" fill="none"/></svg>hello@cedarlooplabs.com</div>
  <div class="contact" style="left:128px;top:248px"><svg viewBox="0 0 8 8"><circle cx="4" cy="4" r="3.4" fill="none" stroke="var(--orange)" stroke-width=".8"/><path d="M.6 4h6.8M4 .6c-2 2-2 4.8 0 6.8M4 .6c2 2 2 4.8 0 6.8" stroke="var(--orange)" stroke-width=".6" fill="none"/></svg>www.cedarlooplabs.com</div>
  <div class="thanks"><strong>THANK YOU</strong><span>For Your time</span></div>
</section>

</body>
</html>
```